Double Sided A4 Bi-Fold Brochure - very clear scope included

I have created a package which outlines the design requirements for an A4 brochure which folds twice to a DL size.

I would like whoever works on this project to look at the plant pictures taken in our reception area and use this for inspiration to style the brochure. So incorporate plants into the them/styling.

In the package you will find page layouts. Text outlines. Price schedules. Grouped pictures.

If you have any questions just ask

Thanks

Target Market(s)

Those seeking medical treatment for injury and chronic disease

Industry/Entity Type

Physical Therapy

Colors
acd036
9bcb3b

Requirements
Must have
• Must have a plant theme (not over powering).
• MUST use the green colours in our Logo.
Nice to have
• Use the pictures that we have included in the package where possible

```html
<!DOCTYPE html>
<html lang="en">
<head>
<meta charset="utf-8">
<title>Steady Physio – Pilates Brochure</title>
<link href="https://fonts.googleapis.com/css2?family=Source+Sans+3:wght@300;400&display=swap" rel="stylesheet">
<style>
:root{
  --green:#8cc63f;
  --green-head:#9bcb3b;
  --lime:#acd036;
  --map-edge:#c4e393;
  --ink:#1e1e1e;
  --white:#fff;
  --rule:#c8c8c8;
}
*{margin:0;padding:0;box-sizing:border-box}
html,body{width:1200px;height:840px;overflow:hidden;background:var(--white)}
body{font-family:"Source Sans 3","Myriad Pro",Arial,sans-serif;color:var(--ink);position:relative}
.abs{position:absolute}

.photo{position:absolute}
.photo-stretch{left:0;top:0;width:398px;height:198px;
  background:linear-gradient(180deg,#efefee 0%,#dcdcda 40%,#a9a9a7 72%,#6d6e70 100%),#ddd}
.photo-studio{left:401px;top:0;width:399px;height:198px;
  background:
    radial-gradient(ellipse 70px 40px at 82% 52%,rgba(150,90,200,.55),rgba(150,90,200,0)),
    radial-gradient(ellipse 60px 35px at 92% 55%,rgba(60,130,200,.5),rgba(60,130,200,0)),
    linear-gradient(180deg,#f2f3f4 0%,#dde0e2 40%,#6d7074 75%,#3e4145 100%)}
.photo-class{left:28px;top:563px;width:743px;height:236px;
  background:
    radial-gradient(ellipse 90px 55px at 88% 82%,rgba(40,130,200,.55),rgba(40,130,200,0)),
    radial-gradient(ellipse 80px 40px at 40% 30%,rgba(50,90,190,.25),rgba(50,90,190,0)),
    linear-gradient(180deg,#f5f5f5 0%,#e7e7e7 45%,#b4b6b8 78%,#6e7073 100%)}

.divider{left:399px;top:198px;width:1px;height:365px;background:var(--rule)}
.heading{font-weight:400;color:var(--green-head);font-size:31px;line-height:1}
.pilates-title{left:29px;top:215px}
.suitable-title{left:428px;top:215px}
.intro{left:30px;top:250px;width:352px;font-size:13.4px;line-height:16.9px}
.suitable-list{top:253px;font-size:13.4px;line-height:15.3px;list-style:none}
.suitable-list li{position:relative;padding-left:16px;margin-bottom:2.2px}
.suitable-list li::before{content:"";position:absolute;left:1px;top:6px;width:4px;height:4px;border-radius:50%;background:var(--ink)}
.list-a{left:428px;width:178px}
.list-b{left:611px;width:185px}
.claim{left:30px;top:397px;width:740px;font-size:13.4px;line-height:15.3px}

.schedule-band{left:260px;top:425px;width:300px;height:32px;
  background:linear-gradient(90deg,rgba(140,198,63,0) 0%,var(--green) 22%,var(--green) 82%,rgba(140,198,63,0) 100%);
  color:var(--white);font-size:29px;line-height:32px;text-align:center}
.schedule{left:121px;top:466px;display:flex;font-size:13.4px;line-height:15.2px}
.schedule .day{width:98px}

.footer-band{left:0;top:810px;width:800px;height:30px;background:linear-gradient(90deg,#f4f9ec 0%,var(--lime) 40%,var(--green) 100%)}
.footer-note{left:418px;top:819px;width:330px;font-size:7.2px;color:var(--white);text-align:center;font-weight:300}

.side{left:800px;top:0;width:400px;height:840px;background:var(--green)}
.side-text{color:var(--white)}
.pricing-title{left:838px;top:50px;font-size:32px;line-height:1;font-weight:400}
.price-head{font-size:16.2px;line-height:20px;font-weight:400}
.price-items{font-size:12.4px;line-height:15.3px;font-weight:300}
.open{left:800px;width:400px;top:442px;text-align:center;font-size:20px;line-height:1;font-weight:400}
.open-days{left:800px;width:400px;top:465px;text-align:center;font-size:16px;font-weight:400}
.open-rule{left:930px;top:494px;width:145px;height:1px;background:rgba(255,255,255,.7)}
.map{left:802px;top:500px;width:398px;height:236px;
  background:linear-gradient(90deg,var(--map-edge) 0%,#eef7e3 18%,#fafdf6 50%,#eef7e3 82%,var(--map-edge) 100%)}
.contact{left:800px;width:400px;top:752px;text-align:center;font-size:12.6px;line-height:15.3px;font-weight:300;font-style:normal}
</style>
</head>
<body>
<div class="photo photo-stretch" role="img" aria-label="Woman stretching her leg on a ballet barre in the studio"></div>
<div class="photo photo-studio" role="img" aria-label="Pilates studio with reformer equipment and exercise balls"></div>
<div class="abs divider"></div>

<h2 class="abs heading pilates-title">Pilates</h2>
<p class="abs intro">All of our individual and group pilates sessions are conducted by highly experienced physiotherapists. All of whom have a minimum of 20 years experience. Clients can progress from individual treatment and management of acute pain, through to strengthening and return to usual activities. Our therapists are always on hand to make adjustments to your exercises and cater for your individual needs, with a professional understanding of your problem.</p>

<h2 class="abs heading suitable-title">Pilates is suitable for:</h2>
<ul class="abs suitable-list list-a">
  <li>Core weakness and starting an exercise programme</li>
  <li>Recovering from injury</li>
  <li>Managing back or neck pain</li>
  <li>Advanced core strengthening</li>
</ul>
<ul class="abs suitable-list list-b">
  <li>Pregnancy and after delivery</li>
  <li>Part of a chronic disease management plan (EPC)</li>
  <li>Posture</li>
  <li>Flexibility</li>
  <li>General exercise</li>
</ul>

<p class="abs claim">Pilates is claimable on your private health insurance extras under your Physiotherapy benefits and we can process your ClaimPoint claim on the spot.</p>

<div class="abs schedule-band">Pilates Schedule</div>
<div class="abs schedule">
  <div class="day">Monday<br>9:15<br>10:15<br>5:30</div>
  <div class="day">Tuesday<br>7:45<br>9:15<br>10:15<br>3:30<br>5:30</div>
  <div class="day">Wednesday<br>9:15<br>10:15<br>11:15<br>5:30</div>
  <div class="day">Thursday<br>7:45<br>9:15<br>10:15<br>11:15</div>
  <div class="day">Friday<br>9:15<br>10:15</div>
  <div class="day">Saturday<br>8:45<br>9:30</div>
</div>

<div class="photo photo-class" role="img" aria-label="Group pilates class on reformers and mats with an instructor"></div>

<div class="abs footer-band"></div>
<div class="abs footer-note">ALL SERVICES CLAIMABLE WITH HEALTH INSURANCE. CLAIMS PROCESSED IMMEDIATELY.</div>

<aside class="abs side"></aside>
<h2 class="abs side-text pricing-title">Pricing</h2>

<div class="abs side-text" style="left:838px;top:87px">
  <div class="price-head">Physio (covered by health insurance)</div>
  <div class="price-items" style="margin-top:2px">Initial = $85 45 minutes<br>Standard = $75 30 minutes<br>Initial Concession = $75<br>Standard Concession = $60<br>Home Visit = $110</div>
</div>

<div class="abs side-text" style="left:838px;top:205px">
  <div class="price-head">Pilates (covered by health insurance)</div>
  <div class="price-items" style="margin-top:1px">$30 each Individually<br>Each as a group of 5 = ($25 X 5) = $125<br>1v1 Pilates = $65<br>Pilates Assessment - $80<br>Kids (14 or Younger) Standard = $75<br>Kids (14 or Younger) = Consession $60</div>
</div>

<div class="abs side-text" style="left:838px;top:327px">
  <div class="price-head">Massage (covered by health insurance)</div>
  <div class="price-items" style="margin-top:3px">1 Hour Massage - $85<br>30 Minutes - $60</div>
</div>

<div class="abs side-text price-items" style="left:838px;top:392px;width:330px">Dry Needling with Acupuncture Needles (covered by health insurance)<br>$90</div>

<div class="abs side-text open">OPEN</div>
<div class="abs side-text open-days">Mon-Saturday</div>
<div class="abs open-rule"></div>

<div class="abs map" role="img" aria-label="Street map showing the clinic location and parking"></div>

<address class="abs side-text contact">4/118 Elm Parade Westfield<br>Ph : 70001234<br>Fax 80005678<br>steadyphysio.com.au</address>
</body>
</html>
```